Tampa Bay fishing guide needs stunning website.

I currently have a site - www.reelcoveguide.example which I personally put together using the Plixo platform and I am looking for a redesign on a different platform (Brindlepress?) that will allow me to easily create landing pages in the future. Would like to have a block for visitors to opt in to newsletter. Need social media links on all pages.
Updates

I would like to let my visitors know that I am able to handle their fishing charter needs here in the Tampa Bay area, if I'm not available for the dates they are looking to go I can refer them to a reputable captain in the area.

Target Market(s)

United States

Industry/Entity Type

Tourism

Coding

Coded - Design and coding required

Number of Pages Required

5+ page

Font styles to use
Sans Serif

Colors
0355a3
3176b5
85abd2
fbf289

Requirements
Must have
• Mobile Responsive, Ability to insert Vantor Metrics, Quillbook pixels, ability to add custom landing pages in future
Nice to have
• Clean, easy navigation

```html
<!DOCTYPE html>
<html lang="en">
<head>
<meta charset="utf-8">
<title>Capt. Cole Brannigan – Tampa Bay Fishing Charters</title>
<link href="https://fonts.googleapis.com/css2?family=Lato:wght@400;700&family=Montserrat:wght@400;500&display=swap" rel="stylesheet">
<style>
:root{
  --blue:#0355a3;
  --blue-mid:#3176b5;
  --blue-light:#85abd2;
  --star:#fbc12d;
  --ink:#111;
  --text:#555;
  --panel:#f3f3f3;
  --footer:#333;
  --white:#fff;
  --gear-light:#8c8570;
  --gear-dark:#3f3f3b;
}
*{margin:0;padding:0;box-sizing:border-box}
html,body{width:1200px;height:2597px;overflow:hidden;background:var(--white)}
body{position:relative;font-family:"Lato",sans-serif;color:var(--text)}
.abs{position:absolute}
h1,h2,h3{font-family:"Montserrat",sans-serif;font-weight:400;color:var(--ink)}

.hero{left:0;top:0;width:1200px;height:615px;background:linear-gradient(180deg,#a9c3de 0%,#d6e2ee 40%,#6d8fb0 62%,#2e4f74 100%)}
.brand{left:76px;top:40px;font-size:38px;font-weight:700;color:var(--blue);letter-spacing:.5px}
.call{left:866px;top:28px;display:flex;align-items:center;gap:16px}
.call-icon{width:48px;height:48px;border-radius:50%;background:var(--blue);display:flex;align-items:center;justify-content:center}
.call-label{font-size:17px;color:#222;line-height:1}
.call-number{font-size:27px;color:var(--blue);font-weight:700;line-height:1.1}

.nav{left:0;top:615px;width:1200px;height:62px;background:var(--blue)}
.nav a{position:absolute;top:0;height:62px;line-height:62px;color:var(--white);font-size:16px;text-decoration:none;font-family:"Montserrat",sans-serif}
.nav .active{background:var(--blue-light);padding:0 28px;left:177px}

.intro{left:0;top:728px;width:1200px;text-align:center}
.intro-kicker{font-size:20px;color:var(--ink);font-family:"Montserrat",sans-serif}
.intro-title{font-size:40px;margin-top:2px}
.intro-copy{width:920px;margin:14px auto 0;font-size:14px;line-height:22.5px}

.panel{left:76px;top:980px;width:1046px;height:262px;background:var(--panel)}
.panel h2{position:absolute;left:66px;top:58px;font-size:27px;line-height:38px;color:#222}
.panel p{position:absolute;left:66px;top:152px;font-size:16px;line-height:26px}
.gear{left:770px;top:950px;width:290px;height:300px;border-radius:24px;background:linear-gradient(150deg,var(--gear-light) 0%,#5f5a4c 50%,var(--gear-dark) 100%)}

.photo-frame{background:var(--white);padding:10px;box-shadow:0 10px 14px -6px rgba(0,0,0,.35)}
.photo-frame div{width:100%;height:100%}
.snook{left:76px;top:1293px;width:501px;height:314px}
.snook div{background:linear-gradient(180deg,#7fb2d8 0%,#9fb9a8 50%,#c23a3a 85%,#4c6f8f 100%)}
.harbor{left:620px;top:1659px;width:504px;height:315px}
.harbor div{background:linear-gradient(180deg,#2f8fd8 0%,#8cc6e8 35%,#8c7a62 60%,#3fb0b8 100%)}

.feature h2{font-size:40px;line-height:42px}
.feature p{font-size:16px;line-height:23px;margin-top:18px}
.btn{display:inline-block;background:var(--blue);color:var(--white);font-size:16px;font-family:"Montserrat",sans-serif;padding:0 18px;height:52px;line-height:52px;text-decoration:none;margin-top:28px}
.charters{left:625px;top:1293px;width:470px}
.pickup{left:110px;top:1659px;width:465px;text-align:right}

.quote-band{left:0;top:2023px;width:1200px;height:292px;background:linear-gradient(90deg,#1f4f87,#2c5f98 50%,#234f86);text-align:center;color:var(--white)}
.quote-mark{width:64px;height:64px;border:2px solid var(--white);border-radius:50%;margin:40px auto 0;font-size:44px;font-family:Georgia,serif;line-height:72px}
.quote-text{width:760px;margin:12px auto 0;font-size:15px;line-height:22px}
.stars{margin-top:8px;color:var(--star);font-size:20px;letter-spacing:1px}
.quote-name{margin-top:6px;font-size:16px;letter-spacing:.5px}
.quote-name em{font-size:14px}

.footer{left:0;top:2315px;width:1200px;height:230px;background:var(--footer);color:var(--white)}
.footer-brand{left:76px;top:40px;font-size:26px;font-weight:700}
.footer-contact{left:76px;top:128px;font-size:16px}
.footer-contact li{list-style:none;display:flex;align-items:center;gap:12px;height:35px}
.footer h3{color:var(--white);font-size:18px;letter-spacing:.5px}
.col{top:43px}
.col-pickup{left:345px}
.col-accept{left:610px;width:230px}
.col-news{left:874px;width:250px}
.col ul{list-style:none;margin-top:14px}
.col li{font-size:14px;height:31px}
.col li:before{content:"» ";}
.col p{font-size:14px;line-height:24px;margin-top:14px}
.cards{display:flex;gap:12px;margin-top:28px}
.cards span{width:46px;height:30px;border-radius:4px;background:var(--white)}
.signup{display:flex;margin-top:26px;width:250px;height:52px}
.signup input{flex:1;border:0;padding:0 18px;font-size:14px;font-style:italic;font-family:"Lato",sans-serif}
.signup button{width:52px;border:0;background:var(--blue-light);display:flex;align-items:center;justify-content:center}

.bottom{left:0;top:2545px;width:1200px;height:52px;background:var(--blue);color:var(--white)}
.copyright{left:78px;top:17px;font-size:13px;letter-spacing:.3px}
.social{left:1040px;top:8px;display:flex;align-items:center;gap:10px;font-size:14px}
.social span{width:36px;height:36px;border-radius:50%;background:var(--blue-mid)}
</style>
</head>
<body>

<div class="abs hero" role="img" aria-label="Smiling angler on a boat holding a large red snapper over open water"></div>
<div class="abs brand">Capt. Cole Brannigan</div>
<div class="abs call">
  <div class="call-icon">
    <svg width="24" height="24" viewBox="0 0 24 24"><path fill="#fff" d="M6.6 10.8a15.2 15.2 0 0 0 6.6 6.6l2.2-2.2c.3-.3.7-.4 1-.2 1.1.4 2.3.6 3.6.6.6 0 1 .4 1 1V20c0 .6-.4 1-1 1A17 17 0 0 1 3 4c0-.6.4-1 1-1h3.5c.6 0 1 .4 1 1 0 1.3.2 2.5.6 3.6.1.3 0 .7-.2 1z"/></svg>
  </div>
  <div>
    <div class="call-label">Call Capt. Cole</div>
    <div class="call-number">(555) 014-2287</div>
  </div>
</div>

<nav class="abs nav">
  <a class="active" href="#">HOME</a>
  <a href="#" style="left:312px">ABOUT US</a>
  <a href="#" style="left:450px">PICK UP LOCATIONS</a>
  <a href="#" style="left:663px">RATES</a>
  <a href="#" style="left:772px">GIFT CARDS</a>
  <a href="#" style="left:923px">CONTACT US</a>
</nav>

<section class="abs intro">
  <div class="intro-kicker">TAMPA BAY, FISHING GUIDE, TAMPA BAY</div>
  <h1 class="intro-title">FISHING CHARTERS</h1>
  <p class="intro-copy">Capt. Cole Brannigan, with over 20 years' experience, Native fishing charter tampa charter captain offering full and half day fishing charters on the waters of Tampa Bay. If you're looking for a great fishing charter tampa don't hesitate to contact Capt. Cole or you can simply book your trip online here. Come enjoy a wonderful day fishing charters Tampa for Tarpon, Snook, Redfish, Trout, Sharks, Cobia, Spanish mackerel as well as others aboard Capt. Cole Brannigan Sport fishing Charters boat. Capt. Cole will work hard to ensure that you and your guests have a memorable day enjoying the wonderful gamefish that Tampa Bay has to offer.</p>
</section>

<section class="abs panel">
  <h2>We Provide all fishing Charter needs here to<br>visitors in the Tampa Bay Area</h2>
  <p>If I'm not available for the dates they are looking to go I can refer them to a<br>reputable captain in the area.</p>
</section>
<div class="abs gear" role="img" aria-label="Fishing rods, landing net and tackle bag"></div>

<div class="abs photo-frame snook"><div role="img" aria-label="Two anglers holding a large snook on the water"></div></div>
<section class="abs feature charters">
  <h2>FULL &amp; HALF DAY<br>CHARTERS</h2>
  <p>Offering Tampa Bay, FL fishing charters on the beautiful waters of Tampa Bay. Fish with Capt. Cole Brannigan, Tampa Bay, FL fishing guide for over 20 years</p>
  <a class="btn" href="#">FIND OUT MORE</a>
</section>

<section class="abs feature pickup">
  <h2>MULTIPLE PICKUP<br>LOCATIONS</h2>
  <p>Whether you're looking for a fishing charter/guide in Tampa, St. Pete, Clearwater or Bradenton, Capt. Cole can pick you up nearby. Click here for maps of pickup locations.</p>
  <a class="btn" href="#">VIEW LOCATIONS</a>
</section>
<div class="abs photo-frame harbor"><div role="img" aria-label="Small boats moored by rocky shore with gulls and hills"></div></div>

<section class="abs quote-band">
  <div class="quote-mark">“</div>
  <p class="quote-text">"Lorem Ipsum is simply dummy text of the printing and typesetting industry. Lorem Ipsum has been the industry's standard dummy text ever since the 1500s, when an unknown printer took a galley."</p>
  <div class="stars">★★★★☆</div>
  <div class="quote-name">KARA SIMMS, <em>Tidewater Outfitters</em></div>
</section>

<footer class="abs footer">
  <div class="abs footer-brand">Capt. Cole Brannigan</div>
  <ul class="abs footer-contact">
    <li><svg width="20" height="20" viewBox="0 0 24 24"><path fill="#fff" d="M6.6 10.8a15.2 15.2 0 0 0 6.6 6.6l2.2-2.2c.3-.3.7-.4 1-.2 1.1.4 2.3.6 3.6.6.6 0 1 .4 1 1V20c0 .6-.4 1-1 1A17 17 0 0 1 3 4c0-.6.4-1 1-1h3.5c.6 0 1 .4 1 1 0 1.3.2 2.5.6 3.6.1.3 0 .7-.2 1z"/></svg><b>555-014-2287</b></li>
    <li><svg width="20" height="14" viewBox="0 0 20 14"><rect width="20" height="14" fill="#fff"/><path d="M0 0l10 8 10-8" fill="none" stroke="#333" stroke-width="1.5"/></svg>captcole@mailbox.example</li>
  </ul>
  <div class="abs col col-pickup">
    <h3>PICKUP LOCATIONS</h3>
    <ul>
      <li>Harbor Point Marina - St. Petersburg</li>
      <li>Sandpiper Dock - Ruskin</li>
      <li>Causeway Boat Ramp</li>
      <li>Pelican Boat Ramp</li>
    </ul>
  </div>
  <div class="abs col col-accept">
    <h3>WE ACCEPT</h3>
    <p>Lorem Ipsum is simply dummy text of the printing and typesetting industry.</p>
    <div class="cards"><span></span><span></span><span></span><span></span></div>
  </div>
  <div class="abs col col-news">
    <h3>NEWSLETTER</h3>
    <p>Subscribe to get News &amp; Updates of our work</p>
    <form class="signup">
      <input type="email" placeholder="E-Mail">
      <button type="button" aria-label="Subscribe"><svg width="20" height="14" viewBox="0 0 20 14"><rect x=".75" y=".75" width="18.5" height="12.5" fill="none" stroke="#0355a3" stroke-width="1.5"/><path d="M1 1l9 7 9-7" fill="none" stroke="#0355a3" stroke-width="1.5"/></svg></button>
    </form>
  </div>
</footer>

<div class="abs bottom">
  <div class="abs copyright">© CAPT. COLE BRANNIGAN - 2016. All Rights Reserved</div>
  <div class="abs social"><span></span>Quillbook</div>
</div>

</body>
</html>
```